Flyer Design Project

A beauty salon Velmora Spa needs a flyer design to promote some new services that are available in the salon. These are anti-aging, slimming and other treatments performed on the modern high-tech cosmetological equipment.
The flyer will be distrubuted in hi-end supermarket located near the salon. It would go inside the bags when the purchases are packed at the cashier desk.
The main idea is make people read it and not to throw it away immediately. The flyer will be printed on the top quality paper.
There will either be a discound or a promotional treatment in the flyer.
We are not sure about the size of the flyer. It should not be too big neither too small. Ideally on the one side there should be information about Facial Treatments and on the other about the Body Treatments. However we are open for other suggestions of the Pixel Throng.
This is our web-site www.velmora-spa.ru
Though being in Russian, it may give you an idea of our concept.
Updates

Thanks for all the designs submitted.

One general comment would be - the flyer should look different from the usual flyer one might get regarding the beauty salon services. Please make it attractive and unusual. Thanks.

Target Market(s)

Ladies from 25 to 60 years old who are well-to-do

Industry/Entity Type

Beauty Salon

Requirements
Nice to have
• It would be nice to have some technical features in the design.
Should not have
• The flyer should not be overloaded with pictures or graphic design features. It should be elegant and clear. The design should not look too "spa" as we promote technological treatments not massages.

```html
<!DOCTYPE html>
<html lang="en">
<head>
<meta charset="utf-8">
<title>Velmora Spa — Flyer</title>
<link rel="stylesheet" href="https://fonts.googleapis.com/css2?family=Didact+Gothic&family=Pinyon+Script&display=swap">
<style>
  :root {
    --backdrop: #140709;
    --brown-deep: #34140f;
    --brown-mid: #5a2518;
    --brown-warm: #7a3a28;
    --wood-dark: #2e1a14;
    --wood-light: #5a3b2f;
    --pink: #e6245a;
    --white: #ffffff;
    --ink: #3a2a26;
  }
  html, body {
    margin: 0; padding: 0;
    width: 1200px; height: 900px;
    overflow: hidden;
    background: var(--backdrop);
    font-family: "Didact Gothic", "Century Gothic", sans-serif;
  }
  .canvas { position: relative; width: 1200px; height: 900px; overflow: hidden; }
  .flyer { position: absolute; overflow: hidden; }
  .flyer > * { position: absolute; }
  .flyer svg.shapes { left: 0; top: 0; }

  .wood {
    background:
      radial-gradient(ellipse at 30% 40%, rgba(255,255,255,0.06), transparent 60%),
      linear-gradient(100deg, var(--wood-dark), var(--wood-light) 45%, var(--wood-dark) 80%, #3d261d);
  }

  .brand {
    display: flex; align-items: center; gap: 10px;
    color: var(--white); white-space: nowrap;
  }
  .brand-dot { width: 0.55em; height: 0.55em; border-radius: 50%; background: var(--white); }
  .brand-name { line-height: 1; }
  .brand-tag { font-size: 0.32em; line-height: 1.05; margin-left: 4px; }

  .script-title {
    font-family: "Pinyon Script", cursive;
    color: var(--pink); margin: 0; font-weight: 400; white-space: nowrap;
    text-shadow: 0 1px 2px rgba(0,0,0,0.4);
  }
  .copy { margin: 0; text-align: justify; }

  /* Body flyer */
  .flyer-body { left: 140px; top: 245px; width: 400px; height: 517px; background: var(--brown-deep); }
  .flyer-body .brand { left: 60px; top: 38px; font-size: 38px; }
  .flyer-body .photo {
    left: 0; top: 150px; width: 400px; height: 161px;
    background: linear-gradient(90deg, #cfd6da, #f1f3f2 40%, #b8c4c9 70%, #e7ecec);
  }
  .flyer-body .wood { left: 0; top: 311px; width: 400px; height: 206px; }
  .flyer-body .script-title { left: 80px; top: 316px; font-size: 29px; }
  .flyer-body .copy {
    left: 50px; top: 350px; width: 222px;
    font-size: 6.6px; line-height: 8.1px; color: var(--white);
    text-align-last: center;
  }

  /* Facial flyer */
  .flyer-facial { left: 604px; top: 27px; width: 539px; height: 698px; background: var(--brown-mid); }
  .flyer-facial .top {
    left: 0; top: 0; width: 539px; height: 260px;
    background: radial-gradient(ellipse at 30% 20%, #9c5a4c, var(--brown-mid) 55%, #4b1d13);
  }
  .flyer-facial .brand { left: 79px; top: 50px; font-size: 50px; }
  .flyer-facial .wood-upper { left: 0; top: 170px; width: 206px; height: 243px; }
  .flyer-facial .photo {
    left: 206px; top: 200px; width: 333px; height: 213px;
    background: radial-gradient(ellipse at 30% 60%, #6d7a86, #c9c2bb 35%, #ede4de 70%);
  }
  .flyer-facial .white-col { left: 0; top: 413px; width: 206px; height: 285px; background: var(--white); }
  .flyer-facial .wood-lower { left: 206px; top: 413px; width: 333px; height: 285px; }
  .flyer-facial .white-col .copy {
    position: absolute; left: 36px; top: 12px; width: 157px;
    font-size: 8.6px; line-height: 12.2px; color: var(--ink);
  }
  .flyer-facial .script-title { left: 216px; top: 410px; font-size: 40px; }
  .flyer-facial .wood-lower .copy {
    position: absolute; left: 16px; top: 48px; width: 306px;
    font-size: 8.6px; line-height: 12.2px; color: var(--white); text-align: left;
  }
  .stripe-clearance {
    float: right; width: 306px; height: 250px;
    shape-outside: polygon(306px 0, 296px 0, 280px 70px, 244px 132px, 190px 186px, 130px 240px, 306px 250px);
  }
</style>
</head>
<body>
<main class="canvas">

  <section class="flyer flyer-body" aria-label="Body Treatments flyer">
    <div class="photo" role="img" aria-label="Photo of a salon display with rows of skincare bottles and jars"></div>
    <div class="wood" role="img" aria-label="Dark wood texture background"></div>
    <svg class="shapes" width="400" height="517" viewBox="0 0 400 517" aria-hidden="true">
      <path d="M0,0 H400 V130 C340,205 250,205 160,170 C100,150 40,150 0,160 Z" fill="#5a2418"/>
      <path d="M0,0 H400 V95 C260,125 110,150 0,118 Z" fill="#34140f"/>
      <path d="M0,112 C110,148 250,122 400,92 L400,108 C260,142 110,168 0,140 Z" fill="#e6245a"/>
    </svg>
    <div class="brand"><span class="brand-dot"></span><span class="brand-name">velmora spa</span><span class="brand-tag">салон<br>красоты</span></div>
    <h2 class="script-title">Body Treatments</h2>
    <p class="copy">Our body programmes combine clinical precision with calm comfort. Modern hardware sculpts contours, smooths skin texture and supports lymphatic flow, so every session brings a visible, measurable result. Each course begins with a skin and body analysis and a plan built around your goals. Slimming, lifting and firming protocols use radiofrequency, cavitation and gentle vacuum technologies tested in leading European clinics. Sessions are short, painless and fit easily into a busy day. Our specialists track progress at every visit and adjust the settings to keep results steady and natural. Combine body contouring with skin renewal for a complete effect before the summer season. Ask our specialists about seasonal courses and the welcome offer for new guests. Book by phone or online and enjoy a complimentary consultation before your first treatment.</p>
  </section>

  <section class="flyer flyer-facial" aria-label="Facial Treatments flyer">
    <div class="top"></div>
    <div class="wood wood-upper" role="img" aria-label="Dark wood texture background"></div>
    <div class="photo" role="img" aria-label="Close-up photo of an eye with long lashes"></div>
    <svg class="shapes" width="539" height="698" viewBox="0 0 539 698" aria-hidden="true">
      <path d="M0,0 H539 V160 C470,175 420,200 390,250 C360,290 300,280 200,250 C120,225 50,200 0,195 Z" fill="#5a2518"/>
      <path d="M0,0 H110 C60,40 30,80 0,95 Z" fill="#1d0a08"/>
      <path d="M0,125 C60,160 140,190 260,180 C360,172 450,165 539,160 L539,185 C440,192 360,210 260,210 C150,212 60,185 0,160 Z" fill="#e6245a"/>
    </svg>
    <div class="brand"><span class="brand-dot"></span><span class="brand-name">velmora spa</span><span class="brand-tag">салон<br>красоты</span></div>
    <div class="white-col">
      <p class="copy">Technology meets care at every step. Our cosmetologists work with certified equipment that reads the skin, adapts each parameter and delivers energy exactly where it is needed. The result is firmer, brighter and visibly younger skin without long recovery. Before each programme we study your skin type, lifestyle and wishes, then build a course that fits your calendar. Anti-aging, lifting, hydration and renewal protocols can be combined for a complete effect. Every guest receives home care advice and a follow-up visit to track progress. Present this flyer at reception to receive a special welcome price on your first facial course.</p>
    </div>
    <div class="wood wood-lower">
      <p class="copy"><span class="stripe-clearance" aria-hidden="true"></span>Our facial programmes use microcurrent, ultrasound and radiofrequency to restore tone and elasticity from within. Each treatment is tailored after a detailed skin diagnosis, so the device settings match your needs precisely. Lifting sessions redefine the oval of the face, while deep hydration protocols return radiance and comfort to tired skin. Renewal treatments refine texture and soften fine lines with no downtime. A full course takes four to eight visits, and first changes show after one session. Ask about our introductory offer and a free consultation. Book today by phone or on our website.</p>
    </div>
    <svg class="shapes" width="539" height="698" viewBox="0 0 539 698" aria-hidden="true">
      <path d="M539,470 C520,570 460,650 360,698 L395,698 C480,650 530,580 539,520 Z" fill="#ffffff"/>
      <path d="M539,560 C525,620 500,665 470,698 L480,698 C510,668 532,625 539,590 Z" fill="#ffffff"/>
      <path d="M539,630 C530,660 518,682 505,698 L512,698 C524,684 534,664 539,648 Z" fill="#ffffff"/>
    </svg>
    <h2 class="script-title">Facial Treatments</h2>
  </section>

</main>
</body>
</html>
```